依頼詳細
Linkvaleページのカバー画像デザインの募集です。
ご存知のようにサイズは851×315で100kB未満のJPEGファイルだと表示が早いという事になっていますが、画像はPNGが良いとの表現もあり、どうなんでしょう?
左下に160x160のプロフィール画像が入ったり、下4分の1にグラデションがかかったりしますので、それらを考慮したデザインとなります。

下のサイトなどが参考になるかもしれませんが、こだわる必要はありません。
http://ja.pagoru.com/blog/2014/03/ビジネスのlinkvaleカバー写真活用/

Webサイトは製造業の生産性、効率が向上するためのコンテンツ提供と、困りごとQ&Aなどが中心です。ターゲットは、中小から大企業まで、電気、機械、化学、食品など製造業であればジャンルを問いません。 中小企業では社長や経営陣、大企業では現場の技術者、管理職が主要な利用者です。

掲載はJPEGですが、後日編集する可能性がありますので、aiファイルも提出願います。

サイトと会社のロゴ画像、パンフレット画像を添付しますので、必要なパーツは流用してください。またスナプリオ(https://jp.snaprio.com/)の権利が多少残っていますので数枚の利用が可能です。
記載項目
サイト名(かざぐるま.com)、サイトロゴ画像、キャッチコピー、(社名は入れなくて可、入れても小さく)
サイズ
• 851×315
希望イメージ
シンプル 複雑
単色 カラフル
暗い 明るい
日常 高級
遊び心 厳粛
未来的 伝統的
女性的 男性的
希望する色
赤系、青系、コーポレートカラーが青メインに赤アクセントです。すべて統一する必要はありませんが。
納品ファイル
• 高解像度JPG (.jpg)
• イラストレーター形式 (.ai)
補足説明
サイトロゴ、会社ロゴ、パンフレット画像を添付しますが、パンフのaiファイルが54MBあるため、jpegを添付しておきます。aiが必要な場合は何か別の提供方法を教えてください。
■ 選んだ理由

たくさんの素晴らしい提案があり迷いましたが、以下の観点で決定しました。
(1)ものづくりの範囲は広いので、一つのイメージに限定されない、複数の画像がまとまりよく配置されていること。
(2)プロファイル画像や、Linkvaleの強制表示とのバランス。
(3)キャッチフレーズ(結局パンフレットと同じものに)
(4)画像がでしゃばりすぎず、ロゴやコピーの視認性が良い。

■ 提案者全員のお礼・コメント

本当にたくさんの人からの多くの提案をいただき感激です。
また時々募集しますので、次回もよろしくお願い致します。

```html
<!DOCTYPE html>
<html lang="ja">
<head>
<meta charset="utf-8">
<title>かざぐるま.com カバー</title>
<link href="https://fonts.googleapis.com/css2?family=Noto+Sans+JP:wght@700;900&display=swap" rel="stylesheet">
<style>
  :root{
    --brand-blue:#1a3a9c;
    --accent-red:#e0141e;
    --ink:#222;
    --band:rgba(255,255,255,0.82);
    --divider:#ffffff;
    --photo-light:#b9b9b9;
    --photo-dark:#3c3c3c;
  }
  html,body{margin:0;padding:0;overflow:hidden;background:#fff;}
  .cover{
    position:relative;width:1200px;height:444px;overflow:hidden;
    font-family:"Noto Sans JP",sans-serif;background:var(--divider);
  }
  .photo{position:absolute;top:0;height:444px;}
  .photo--gears{left:0;width:294px;background:linear-gradient(160deg,#cfcfcf 0%,#6a6a6a 55%,#2e2e2e 100%);}
  .photo--workbench{left:298px;width:296px;background:linear-gradient(180deg,#d8d8d8 0%,#9a9a9a 50%,#555 100%);}
  .photo--circuit{left:598px;width:300px;background:linear-gradient(200deg,#a8a8a8 0%,#5a5a5a 50%,#2a2a2a 100%);}
  .photo--lathe{left:902px;width:298px;background:linear-gradient(170deg,#c4c4c4 0%,#7a7a7a 55%,#3a3a3a 100%);}
  .band{position:absolute;left:0;top:138px;width:1200px;height:114px;background:var(--band);}
  .site-name{
    position:absolute;left:48px;top:166px;display:flex;align-items:center;gap:12px;
    color:var(--brand-blue);font-weight:900;font-size:38px;letter-spacing:1px;
  }
  .site-name__mark{width:46px;height:46px;border-radius:50%;background:var(--brand-blue);}
  .catch{position:absolute;left:522px;top:150px;margin:0;font-weight:900;color:var(--brand-blue);font-size:25px;line-height:40px;letter-spacing:1px;}
  .catch .red{color:var(--accent-red);}
  .catch .small{color:var(--ink);font-size:18px;}
  .free-badge{
    position:absolute;left:990px;top:130px;width:128px;height:128px;border-radius:50%;
    background:radial-gradient(circle at 38% 30%,#ff7a6a 0%,#ee2a1e 40%,#b80c0c 100%);
    color:#fff;font-weight:900;font-size:17px;line-height:26px;text-align:center;
    display:flex;align-items:center;justify-content:center;
  }
</style>
</head>
<body>
<div class="cover">
  <div class="photo photo--gears" role="img" aria-label="モノクロ写真:機械の歯車"></div>
  <div class="photo photo--workbench" role="img" aria-label="モノクロ写真:作業台で組立作業をする技術者"></div>
  <div class="photo photo--circuit" role="img" aria-label="モノクロ写真:電子回路基板のクローズアップ"></div>
  <div class="photo photo--lathe" role="img" aria-label="モノクロ写真:旋盤を操作する作業者"></div>

  <div class="band"></div>

  <div class="site-name"><span class="site-name__mark"></span>かざぐるま.com</div>

  <p class="catch">
    製造業<span class="small">の</span><span class="red">問題解決</span><span class="small">を</span><span class="red">支援</span><span class="small">する</span><br>
    日本最大級<span class="small">の</span>ポータルサイト
  </p>

  <div class="free-badge">利用・登録<br>すべて無料</div>
</div>
</body>
</html>
```